Flyer-Design für Coaching & Beratung
Zielgruppe
Coaching & Beratung in Betrieben und von Privatpersonen. Das Coaching ist Werte orientiert.
Zielgruppe: KMU (Führungskräfte) und Privatpersonen
Aufgabenstellung
Bitte Beschreibung Flyer beachten (Datei).
6-Seitiges Flyer, in quadratischer Form 10cm x 10cm

```html
<!DOCTYPE html>
<html lang="de">
<head>
<meta charset="utf-8">
<title>Flyer – Coaching &amp; Beratung</title>
<link rel="stylesheet" href="https://fonts.googleapis.com/css2?family=Open+Sans:wght@300;400;600;700&display=swap">
<style>
  :root {
    --green: #617d3a;
    --brown: #6e5448;
    --text: #3f3f3f;
    --heading: #4a4f55;
    --paper: #ffffff;
  }
  * { margin: 0; padding: 0; box-sizing: border-box; }
  html, body { width: 1200px; height: 400px; overflow: hidden; background: var(--paper); }
  body { font-family: "Open Sans", Arial, sans-serif; color: var(--text); position: relative; }

  .cover { position: absolute; left: 0; top: 0; width: 401px; height: 400px; background: var(--paper); }
  .cover__band { position: absolute; left: 0; width: 100%; background: var(--green); }
  .cover__band--top { top: 0; height: 56px; }
  .cover__band--thin { top: 60px; height: 8px; }
  .cover__band--bottom { top: 241px; height: 159px; }

  .brand { position: absolute; left: 17px; top: 85px; width: 370px; height: 142px; }
  .brand__mark { position: absolute; left: 0; top: 0; }
  .brand__name {
    position: absolute; left: 171px; top: 28px;
    color: var(--brown); font-weight: 700; text-transform: uppercase;
    font-size: 24px; line-height: 30px; letter-spacing: 2px;
  }
  .brand__rule { position: absolute; left: 171px; top: 96px; width: 198px; height: 2px; background: var(--brown); }
  .brand__tagline {
    position: absolute; left: 171px; top: 104px;
    color: var(--brown); font-weight: 700; font-size: 14px; letter-spacing: 0.3px;
  }

  .cover__menu { position: absolute; left: 20px; top: 318px; list-style: none; }
  .cover__menu li { color: var(--paper); font-size: 11px; font-weight: 600; line-height: 24.6px; }

  .panel { position: absolute; top: 0; height: 400px; }
  .panel--business { left: 421px; width: 380px; }
  .panel--private { left: 821px; width: 370px; }

  .panel__marker { position: absolute; top: 0; }
  .panel--business .panel__marker { left: 54px; }
  .panel--private .panel__marker { left: 96px; }

  .panel__title {
    position: absolute; left: 0; top: 29px;
    font-size: 17.5px; font-weight: 600; color: var(--heading); letter-spacing: 0.2px;
  }
  .panel__topics { position: absolute; left: 0; list-style: none; width: 160px; }
  .panel--business .panel__topics { top: 65px; }
  .panel--private .panel__topics { top: 69px; }
  .panel__topics li {
    position: relative; padding-left: 13.5px;
    color: var(--green); font-size: 11px; line-height: 14.9px;
  }
  .panel__topics li::before { content: "·"; position: absolute; left: 0; color: var(--green); }

  .panel__figure { position: absolute; background: var(--green); opacity: 0.9; border-radius: 20px 20px 4px 4px; }
  .panel--business .panel__figure { left: 0; top: 186px; width: 146px; height: 99px; }
  .panel--private .panel__figure { left: 47px; top: 254px; width: 74px; height: 119px; }

  .panel__divider { position: absolute; top: 68px; width: 1px; height: 307px; background: var(--green); }
  .panel--business .panel__divider { left: 165px; }
  .panel--private .panel__divider { left: 159px; }

  .panel__copy { position: absolute; top: 66px; font-size: 11px; line-height: 14.9px; font-weight: 300; color: var(--text); }
  .panel--business .panel__copy { left: 178px; width: 192px; }
  .panel--private .panel__copy { left: 173px; width: 190px; }
  .panel__copy p + p { margin-top: 14.9px; }

  .panel__seal { position: absolute; left: 296px; top: 321px; }
</style>
</head>
<body>

<section class="cover">
  <div class="cover__band cover__band--top"></div>
  <div class="cover__band cover__band--thin"></div>

  <div class="brand">
    <svg class="brand__mark" width="154" height="142" viewBox="0 0 154 142" aria-hidden="true">
      <circle cx="77" cy="71" r="68" fill="none" stroke="var(--brown)" stroke-width="2"/>
    </svg>
    <div class="brand__name">Lorenz<br>Haberland</div>
    <div class="brand__rule"></div>
    <div class="brand__tagline">COACHING &amp; BERATUNG</div>
  </div>

  <div class="cover__band cover__band--bottom"></div>
  <ul class="cover__menu">
    <li>BUSINESS COACHING</li>
    <li>PRIVATPERSONEN COACHING</li>
    <li>TELEFON &amp; ONLINECOACHING</li>
  </ul>
</section>

<section class="panel panel--business">
  <svg class="panel__marker" width="53" height="26" viewBox="0 0 53 26" aria-hidden="true">
    <polygon points="0,0 53,0 26.5,26" fill="var(--brown)"/>
  </svg>
  <h2 class="panel__title">BUSINESS COACHING</h2>
  <ul class="panel__topics">
    <li>Führungskräfte Entwicklung</li>
    <li>Führungskräfte Begleitung</li>
    <li>Veränderungsprozesse</li>
    <li>Umgang mit Stress</li>
    <li>Kommunikation</li>
  </ul>
  <div class="panel__figure" role="img" aria-label="Silhouetten einer Gruppe von fünf Geschäftsleuten"></div>
  <div class="panel__divider"></div>
  <div class="panel__copy">
    <p>Nicht nur die Fach- und Methoden­kompetenz ist bei Führungskräften wichtig. Im Umgang mit Mitarbei­tenden ist der Führungsstiel ebenso wichtig, wenn nicht sogar wichtiger. Motivation, Lob und Anerkennung bei Mitarbeitenden steigert deren Leistung nachhaltig und somit die Produktivität.</p>
    <p>Wie Führungskräfte mit Stress und Veränderungen umgehen, überträgt sich auf die Mitarbeiterschaft. Es kann ungewollt Widerstände und Demotivationen auslösen. Glaubwür­dig und authentisch führen, hierbei möchte ich Sie gerne unterstützen und begleiten.</p>
    <p>Führung fängt bei einem selber an. Wie führen Sie sich?</p>
  </div>
</section>

<section class="panel panel--private">
  <svg class="panel__marker" width="53" height="26" viewBox="0 0 53 26" aria-hidden="true">
    <polygon points="0,0 53,0 26.5,26" fill="var(--brown)"/>
  </svg>
  <h2 class="panel__title">PRIVATPERSONEN COACHING</h2>
  <ul class="panel__topics">
    <li>Beziehungsthemen</li>
    <li>Gewohnheiten/<br>Verhalten verändern</li>
    <li>Denkblockaden lösen</li>
    <li>Berufliche Neuorientierung</li>
  </ul>
  <div class="panel__figure" role="img" aria-label="Silhouetten eines Mannes und einer Frau"></div>
  <div class="panel__divider"></div>
  <div class="panel__copy">
    <p>Manchmal meinst du etwas anders, als es verstanden wird. Oder gibt es vielleicht Dinge, welche dich in deiner Beziehung auf die Palme bringen?</p>
    <p>Vielleicht merkst du, daß dein Verhalten oder deine Gewohnheiten nicht immer passend sind.</p>
    <p>Wenn dir diese oder ähnliche Situa­tionen bekannt vorkommen und du daran etwas ändern möchtest, kön­nen wir gemeinsam daran arbeiten.</p>
  </div>
  <svg class="panel__seal" width="62" height="56" viewBox="0 0 62 56" aria-hidden="true">
    <circle cx="31" cy="28" r="26" fill="none" stroke="var(--brown)" stroke-width="1.5"/>
  </svg>
</section>

</body>
</html>
```